依頼詳細
分譲マンションのバルコニーの清掃のサービスをします。Before / After等の写真を載せ、プロにお願いするとこんなにも綺麗になるんだと自分で清掃するよりも魅力を感じてもらう為にもサービスを受けたいと思っていただけるようなチラシを作成していただきたいです。
記載項目
社名:株式会社ヨルダ
電話番号:06-6381-7942
住所:大阪市中央区朝霧町2-8-3
QRコード:作成次第送付します。
使用写真:添付
見出し:39(サンキュー)キャンペーン(オシャレな感じで文字ってください)
載せてほしい文言
・当社独自のバルコニークリーニング
・今、このチラシを受け取った
・このチラシを見ているあなた!今なら良いマンション作りに向けたアンケートにご協力していただいた方には、通常13,000円(税込)⇒なんと、3,900円(税込)!!
・作業時間:1H
・何かキャラクター等使用して吹き出しで、気になる箇所全て私達にお申し出ください!!
と記載してください。
自分の中のイメージ図を添付しますが、全然変更してもらっても大丈夫です。オシャレな感じに作成をお願いします。
サイズ
A4
ページ数
片面
希望イメージ
シンプル 複雑
単色 カラフル
暗い 明るい
日常 高級
遊び心 厳粛
未来的 伝統的
女性的 男性的
希望する色
水色系
納品ファイル
• イラストレーター形式 (.ai)
補足説明

私が求めているようなデザインを考案していただきました。

この度はありがとうございました。
どれも魅力的なものばかりで選定するのも困るくらいでした。
今後もお世話になるかと思いますので何卒宜しくお願い致します。

```html
<!DOCTYPE html>
<html lang="ja">
<head>
<meta charset="utf-8">
<title>ベランダクリーニング サンキューキャンペーン</title>
<link href="https://fonts.googleapis.com/css2?family=M+PLUS+Rounded+1c:wght@500;800;900&family=Noto+Sans+JP:wght@500;700;900&display=swap" rel="stylesheet">
<style>
  :root{
    --sky-deep:#1a58b4;
    --sky-mid:#3d8de0;
    --sky-light:#a6d6f6;
    --navy:#16305f;
    --white:#ffffff;
    --yellow:#ffe93b;
    --orange:#e8521f;
    --red:#e8322c;
    --ink:#1f2a3d;
  }
  *{margin:0;padding:0;box-sizing:border-box;}
  html,body{width:846px;height:1200px;overflow:hidden;background:#fff;}
  body{font-family:"Noto Sans JP",sans-serif;color:var(--ink);}
  .flyer{position:relative;width:846px;height:1200px;overflow:hidden;
    background:linear-gradient(180deg,var(--sky-deep) 0%,var(--sky-mid) 30%,var(--sky-light) 58%,#e4f2fc 80%,#fff 88%);}
  .abs{position:absolute;}

  .limited-bubble{left:96px;top:12px;width:136px;height:90px;border-radius:50%;background:var(--white);
    color:var(--sky-deep);font-weight:900;font-size:13px;line-height:1.4;text-align:center;
    display:flex;align-items:center;justify-content:center;}
  .tagline{left:100px;top:160px;background:var(--navy);color:var(--white);font-weight:900;font-size:20px;
    padding:3px 16px;letter-spacing:1px;transform:skewX(-8deg);}
  .pro{left:500px;top:54px;font-family:"M PLUS Rounded 1c",sans-serif;font-weight:900;color:var(--white);
    -webkit-text-stroke:6px var(--navy);paint-order:stroke fill;line-height:1;}
  .pro .big{font-size:120px;letter-spacing:-4px;}
  .pro .small{font-size:52px;}
  .headline{left:40px;top:190px;font-family:"M PLUS Rounded 1c",sans-serif;font-weight:900;font-size:178px;
    color:var(--white);letter-spacing:-6px;-webkit-text-stroke:8px var(--navy);paint-order:stroke fill;line-height:1.1;}
  .pro-photo{left:664px;top:284px;width:166px;height:178px;border-radius:50%;border:5px solid var(--white);
    background:linear-gradient(135deg,#d7dde2,#8a939c);}
  .campaign{left:262px;top:448px;font-family:"M PLUS Rounded 1c",sans-serif;font-weight:900;color:var(--yellow);
    font-size:44px;line-height:1.12;transform:rotate(-5deg);-webkit-text-stroke:5px var(--orange);paint-order:stroke fill;}

  .photo{border:3px solid var(--white);}
  .balcony-view{left:28px;top:580px;width:380px;height:200px;background:linear-gradient(180deg,#a9d0ef,#dce8f1 50%,#b9b3a7);}
  .time-box{left:96px;top:604px;background:var(--white);padding:5px 14px;text-align:center;}
  .time-box .label{font-weight:900;font-size:20px;color:var(--sky-deep);}
  .time-box .note{font-size:10px;color:var(--ink);font-weight:700;}
  .before-photo{left:410px;top:580px;width:212px;height:294px;background:linear-gradient(180deg,#e6e3dc 0%,#c4c1b9 30%,#5e5a53 32%,#4a4640);}
  .after-photo{left:620px;top:580px;width:212px;height:294px;background:linear-gradient(180deg,#e6e3dc 0%,#c4c1b9 30%,#8d9094 32%,#6f7276);}
  .tag{width:98px;height:46px;border-radius:50%;background:var(--white);font-family:"M PLUS Rounded 1c",sans-serif;
    font-weight:800;font-size:22px;color:var(--ink);display:flex;align-items:center;justify-content:center;}
  .before-tag{left:448px;top:808px;}
  .after-tag{left:690px;top:780px;}
  .arrow{left:556px;top:796px;}

  .floor-photo{left:28px;top:790px;width:380px;height:226px;background:linear-gradient(135deg,#969ba1,#60666d);}
  .ask-bubble{left:150px;top:816px;width:196px;height:86px;border-radius:50%;background:var(--white);
    font-weight:700;font-size:13px;line-height:1.45;text-align:center;display:flex;align-items:center;justify-content:center;}
  .offer{left:424px;top:912px;width:400px;font-weight:900;font-size:14.5px;line-height:1.7;color:var(--ink);}
  .special{left:494px;top:982px;background:var(--red);color:var(--white);font-weight:700;font-size:15px;padding:2px 12px;}
  .regular{left:424px;top:1024px;font-size:11px;font-weight:700;}
  .price{left:598px;top:966px;font-family:"M PLUS Rounded 1c",sans-serif;font-weight:900;color:var(--red);
    font-size:66px;line-height:1;letter-spacing:-1px;}
  .price .tax{font-size:13px;letter-spacing:0;}

  .mascot{left:16px;top:946px;width:150px;height:166px;border-radius:12px;
    background:linear-gradient(180deg,#e8f3fc,#9cc8f0);}
  .footer{left:0;top:1120px;width:846px;height:80px;padding:0 40px;display:flex;align-items:center;gap:18px;}
  .footer .company{font-weight:900;font-size:20px;color:var(--navy);}
  .footer .tel{font-family:"M PLUS Rounded 1c",sans-serif;font-weight:900;font-size:28px;color:var(--sky-deep);}
  .footer .addr{font-size:12px;font-weight:500;color:var(--ink);}
</style>
</head>
<body>
<main class="flyer">
  <div class="abs limited-bubble">今このチラシを<br>受け取った<br>アナタ限定!</div>
  <div class="abs tagline">当社独自のベランダクリーニング</div>
  <div class="abs pro"><span class="big">プロ</span><span class="small">の</span></div>
  <h1 class="abs headline">お掃除</h1>
  <div class="abs pro-photo" role="img" aria-label="バルコニー清掃後の床と手すりの写真"></div>
  <p class="abs campaign">サンキュー<br>キャンペーン実施中!</p>

  <div class="abs photo balcony-view" role="img" aria-label="街並みを望むきれいなバルコニーの写真"></div>
  <div class="abs time-box"><div class="label">作業時間1時間</div><div class="note">バルコニーをしっかり清掃</div></div>
  <div class="abs photo before-photo" role="img" aria-label="清掃前の汚れたバルコニー床と室外機の写真"></div>
  <div class="abs photo after-photo" role="img" aria-label="清掃後のきれいなバルコニー床と室外機の写真"></div>
  <div class="abs tag before-tag">Before</div>
  <svg class="abs arrow" width="120" height="30" viewBox="0 0 120 30" aria-hidden="true"><path d="M4 20 Q60 26 116 10M104 4l12 6-10 10" stroke="#ffffff" stroke-width="4" fill="none" stroke-linecap="round"/></svg>
  <div class="abs tag after-tag">After</div>

  <div class="abs photo floor-photo" role="img" aria-label="清掃後のバルコニー床面の写真"></div>
  <div class="abs ask-bubble">気になる箇所全て<br>私達にお申し付け<br>ください!</div>
  <p class="abs offer">このチラシを見ているあなた!今なら良いマンションづくりに向けたアンケートにご協力頂いた方限定</p>
  <div class="abs special">特別価格</div>
  <div class="abs regular">通常価格 13,000円(税込)</div>
  <div class="abs price">¥3,900<span class="tax">(税込)</span></div>

  <div class="abs mascot" role="img" aria-label="吹き出しで話す清掃スタッフのキャラクターイラスト"></div>
  <footer class="abs footer">
    <svg width="32" height="32" viewBox="0 0 24 24" aria-hidden="true"><path fill="#1a58b4" d="M6.6 10.8a15 15 0 006.6 6.6l2.2-2.2c.3-.3.7-.4 1-.2 1.1.4 2.3.6 3.6.6.6 0 1 .4 1 1V20c0 .6-.4 1-1 1C10.6 21 3 13.4 3 4c0-.6.4-1 1-1h3.5c.6 0 1 .4 1 1 0 1.3.2 2.5.6 3.6.1.3 0 .7-.2 1z"/></svg>
    <span class="tel">06-6381-7942</span>
    <div><div class="company">株式会社ヨルダ</div><div class="addr">大阪市中央区朝霧町2-8-3</div></div>
  </footer>
</main>
</body>
</html>
```